Personal creative Biz Card Design

Need personal yet natural and organic design. The cards I have now are well designed but look too commercial. I want more organic FEELING kind of card. I thought having a headshot would make it more personal... but maybe a sketch effect (or line drawing effect) of face better (?). Maybe in a gray or tungsten color?

Target Market(s)

Well, everyone i give card to will have already seen me face-to-face so that is one thing. Mostly yoga students and people interested in improving their fitness or general health. People looking for wellness, a personal fitness trainer, a yoga teacher

Industry/Entity Type

Health And Wellness

Contact Information for Business Card

I provided examples

Requirements
Must have
• My main logo
• My name

```html
<!DOCTYPE html>
<html lang="en">
<head>
<meta charset="utf-8">
<title>Noel Varga – Business Cards</title>
<link rel="stylesheet" href="https://fonts.googleapis.com/css2?family=Open+Sans:wght@300;400;600;700&display=swap">
<style>
  :root {
    --stage: #efece6;
    --leaf-green: #4f9a3b;
    --leaf-green-dark: #44892f;
    --paper: #ffffff;
    --ink: #333333;
    --ink-soft: #666666;
    --card-shadow: 0 14px 30px rgba(0, 0, 0, 0.22);
  }
  * { box-sizing: border-box; margin: 0; padding: 0; }
  html, body {
    width: 1200px;
    height: 900px;
    overflow: hidden;
    background: var(--stage);
    font-family: "Open Sans", Arial, sans-serif;
  }
  .canvas {
    position: relative;
    width: 1200px;
    height: 900px;
  }
  .card {
    position: absolute;
    width: 620px;
    height: 354px;
    box-shadow: var(--card-shadow);
    overflow: hidden;
  }

  /* Front: green card */
  .card-front {
    left: 110px;
    top: 110px;
    background: linear-gradient(135deg, var(--leaf-green) 0%, var(--leaf-green-dark) 100%);
  }
  .card-front .brand-block {
    position: absolute;
    right: 46px;
    top: 110px;
  }
  .card-front .brand-name {
    font-weight: 700;
    font-size: 40px;
    letter-spacing: 0.5px;
    color: var(--paper);
    line-height: 1;
  }
  .card-front .brand-tagline {
    margin-top: 8px;
    font-weight: 300;
    font-size: 16px;
    color: var(--paper);
  }

  /* Back: white card */
  .card-back {
    left: 470px;
    top: 420px;
    background: var(--paper);
  }
  .card-back .brand-block {
    position: absolute;
    left: 150px;
    top: 58px;
    display: flex;
    align-items: center;
    gap: 14px;
  }
  .card-back .brand-dot {
    width: 40px;
    height: 40px;
    border-radius: 50%;
    background: var(--leaf-green);
    flex: none;
  }
  .card-back .brand-name {
    font-weight: 700;
    font-size: 44px;
    color: var(--leaf-green);
    line-height: 1;
  }
  .card-back .brand-tagline {
    margin-top: 6px;
    font-weight: 300;
    font-size: 17px;
    color: var(--ink-soft);
  }
  .card-back .person {
    position: absolute;
    left: 60px;
    top: 178px;
  }
  .person-name {
    font-weight: 600;
    font-size: 26px;
    color: var(--leaf-green);
    line-height: 1.1;
  }
  .person-role {
    font-size: 21px;
    color: var(--ink);
    line-height: 1.2;
  }
  .contact-list {
    list-style: none;
    margin-top: 16px;
  }
  .contact-item {
    display: flex;
    align-items: center;
    gap: 12px;
    font-size: 19px;
    color: var(--ink);
    line-height: 1.55;
  }
  .contact-icon {
    width: 18px;
    height: 18px;
    flex: none;
  }
</style>
</head>
<body>
<main class="canvas">

  <section class="card card-front" aria-label="Business card front">
    <div class="brand-block">
      <p class="brand-name">NOEL VARGA</p>
      <p class="brand-tagline">Steady Support for a Balanced Life</p>
    </div>
  </section>

  <section class="card card-back" aria-label="Business card back">
    <div class="brand-block">
      <span class="brand-dot" aria-hidden="true"></span>
      <div>
        <p class="brand-name">NOEL VARGA</p>
        <p class="brand-tagline">Steady Support for a Balanced Life</p>
      </div>
    </div>

    <div class="person">
      <p class="person-name">Add Name</p>
      <p class="person-role">Teacher of Yoga</p>
      <ul class="contact-list">
        <li class="contact-item">
          <svg class="contact-icon" viewBox="0 0 24 24" aria-hidden="true">
            <path fill="#4f9a3b" d="M6.6 10.8a15 15 0 0 0 6.6 6.6l2.2-2.2a1 1 0 0 1 1-.25 11.4 11.4 0 0 0 3.6.57 1 1 0 0 1 1 1V20a1 1 0 0 1-1 1A17 17 0 0 1 3 4a1 1 0 0 1 1-1h3.5a1 1 0 0 1 1 1c0 1.25.2 2.450.57 3.6a1 1 0 0 1-.25 1z"/>
          </svg>
          555-310-2487
        </li>
        <li class="contact-item">
          <svg class="contact-icon" viewBox="0 0 24 24" aria-hidden="true">
            <g fill="none" stroke="#4f9a3b" stroke-width="2">
              <circle cx="12" cy="12" r="9"/>
              <ellipse cx="12" cy="12" rx="4" ry="9"/>
              <line x1="3" y1="12" x2="21" y2="12"/>
            </g>
          </svg>
          www.noelvarga.com
        </li>
        <li class="contact-item">
          <svg class="contact-icon" viewBox="0 0 24 24" aria-hidden="true">
            <text x="12" y="18" text-anchor="middle" font-size="20" font-weight="700" fill="#4f9a3b" font-family="Open Sans, sans-serif">@</text>
          </svg>
          noelinnerpath@mail.com
        </li>
      </ul>
    </div>
  </section>

</main>
</body>
</html>
```